TUMBLAVERA

We are a group of friends with a passion for ancestral knowledge of potions and medicinal formulas derived from nature. We specialise in medicinal mushrooms and adaptogens. We designed a few supplement formulas which we want to release to the market. Our team comes from biology and nutritional science background. Every product we launch will be clean in biodegradable packaging.
Our first product is a lab-tested grass-fed bovine collagen type I, II, and III mixed with organic lab-tested the most potent and bioavailable medicinal mushrooms on the market. This product will be in a pouch the print will be on the pouch or on a label, we don't know if it's possible to design a label that could be used on both? We don't know if we will be able to use organic labels yet due to the legislation changes in the UK. We are waiting for clarification.
The company is called Brindle Cove. We want to use forgotten ancestral knowledge of those potions and reintroduce them to the people. We would like our brand to look clean and friendly. A natural mix of modern and ancestral design.
Our logo and brand designs we like are attached. I have attached the source file of our logo if anyone thinks colours could be different we are open to ideas. I have also attached the visual design we were playing with on canva.com.

```html
<!DOCTYPE html>
<html lang="en">
<head>
<meta charset="utf-8">
<title>Tumblavera pouch fronts</title>
<link rel="stylesheet" href="https://fonts.googleapis.com/css2?family=Oswald:wght@300;400;700&family=Roboto+Condensed:wght@700&family=Poppins:wght@600&family=Open+Sans:wght@700&display=swap">
<style>
  :root {
    --stage-left: #cfcecb;
    --stage-right: #e0d9cf;
    --brown-light: #8a5c42;
    --brown-dark: #4b2b1d;
    --brown-ink: #5a3a28;
    --orange: #f19a3e;
    --white: #ffffff;
    --pouch-white: #f4f4f4;
    --pouch-grey: #dcdedd;
    --green: #3b8a12;
    --green-bright: #56b31a;
    --ink: #222222;
  }
  * { box-sizing: border-box; margin: 0; padding: 0; }
  html, body { width: 1200px; height: 870px; overflow: hidden; }
  body { display: flex; }
  .stage { width: 600px; height: 870px; display: flex; align-items: center; justify-content: center; }
  .stage--brown { background: var(--stage-left); }
  .stage--white { background: var(--stage-right); }

  .pouch { position: relative; width: 440px; height: 720px; overflow: hidden; border-radius: 6px; }
  .pouch--brown { background: linear-gradient(140deg, var(--brown-light), var(--brown-dark)); }
  .pouch--white { background: linear-gradient(140deg, var(--pouch-white), var(--pouch-grey) 60%, var(--pouch-white)); }

  .shield { position: absolute; left: 135px; top: 0; width: 170px; height: 190px;
    clip-path: polygon(0 0, 100% 0, 100% 78%, 50% 100%, 0 78%);
    display: flex; flex-direction: column; align-items: center; justify-content: center; gap: 10px; padding-bottom: 30px; }
  .pouch--brown .shield { background: var(--white); }
  .pouch--white .shield { background: var(--green); }
  .brand-dot { width: 26px; height: 26px; border-radius: 50%; }
  .brand-name { font-family: "Poppins", sans-serif; font-weight: 600; font-size: 21px; white-space: nowrap; }
  .pouch--brown .brand-dot, .pouch--brown .brand-name { color: var(--orange); background: none; }
  .pouch--brown .brand-dot { background: var(--orange); }
  .pouch--white .brand-name { color: var(--white); }
  .pouch--white .brand-dot { background: var(--white); }

  .product-name { position: absolute; top: 215px; width: 100%; text-align: center;
    font-family: "Oswald", sans-serif; font-weight: 700; font-size: 78px; line-height: 1; letter-spacing: 1px; }
  .pouch--brown .name-a { color: var(--white); }
  .pouch--brown .name-b { color: var(--orange); }
  .pouch--white .name-a { color: var(--green); }
  .pouch--white .name-b { color: var(--ink); }

  .tagline { position: absolute; top: 310px; width: 100%; text-align: center;
    font-family: "Roboto Condensed", sans-serif; font-weight: 700; font-size: 19px; }
  .pouch--brown .tagline { color: var(--orange); }
  .pouch--brown .tagline-accent { color: var(--white); }
  .pouch--white .tagline { color: var(--ink); }
  .pouch--white .tagline-accent { color: var(--green); }

  .spec-pill { position: absolute; top: 346px; left: 95px; width: 250px; height: 28px;
    clip-path: polygon(12px 0, calc(100% - 12px) 0, 100% 50%, calc(100% - 12px) 100%, 12px 100%, 0 50%);
    font-family: "Oswald", sans-serif; font-weight: 400; font-size: 15px; line-height: 28px; text-align: center; }
  .pouch--brown .spec-pill { background: var(--white); color: var(--brown-ink); }
  .pouch--white .spec-pill { background: var(--ink); color: var(--white); }

  .mushroom-art { position: absolute; top: 400px; left: 140px; width: 160px; height: 160px; border-radius: 50% 50% 12px 12px; }
  .pouch--brown .mushroom-art { background: linear-gradient(180deg, var(--orange), #b86d2a); opacity: .85; }
  .pouch--white .mushroom-art { background: linear-gradient(180deg, var(--green-bright), var(--green)); opacity: .8; }

  .claims-band { position: absolute; top: 565px; left: 0; width: 100%; height: 78px;
    display: flex; justify-content: center; gap: 34px; align-items: center; }
  .pouch--brown .claims-band { background: var(--white); border-top: 5px solid var(--orange); }
  .pouch--white .claims-band { background: linear-gradient(90deg, var(--green), var(--green-bright)); border-top: 5px solid var(--ink); }
  .claim { display: flex; flex-direction: column; align-items: center; gap: 4px; width: 60px; }
  .claim-mark { width: 38px; height: 38px; border-radius: 50%; }
  .pouch--brown .claim-mark { border: 3px solid var(--brown-ink); }
  .pouch--white .claim-mark { border: 3px solid var(--white); }
  .claim-label { font-family: "Open Sans", sans-serif; font-weight: 700; font-size: 7px; text-align: center; line-height: 1.1; }
  .pouch--brown .claim-label { color: var(--brown-ink); }
  .pouch--white .claim-label { color: var(--white); }

  .net-weight { position: absolute; top: 672px; width: 100%; text-align: center;
    font-family: "Open Sans", sans-serif; font-weight: 700; font-size: 13px; }
  .pouch--brown .net-weight { color: var(--white); }
  .pouch--white .net-weight { color: var(--ink); }
</style>
</head>
<body>
  <section class="stage stage--brown">
    <article class="pouch pouch--brown">
      <div class="shield"><span class="brand-dot"></span><span class="brand-name">Brindle Cove</span></div>
      <h1 class="product-name"><span class="name-a">TUMB</span><span class="name-b">LAVERA</span></h1>
      <p class="tagline">Collagen Peptides &amp; <span class="tagline-accent">Medicinal Mushrooms</span></p>
      <p class="spec-pill">- TYPE I, II, III | UNFLAVOURED -</p>
      <div class="mushroom-art" role="img" aria-label="Illustration of a cluster of medicinal mushrooms"></div>
      <ul class="claims-band">
        <li class="claim"><span class="claim-mark"></span><span class="claim-label">SUGAR<br>FREE</span></li>
        <li class="claim"><span class="claim-mark"></span><span class="claim-label">GLUTEN<br>FREE</span></li>
        <li class="claim"><span class="claim-mark"></span><span class="claim-label">LAB<br>TESTED</span></li>
        <li class="claim"><span class="claim-mark"></span><span class="claim-label">100%<br>RECYCLABLE</span></li>
      </ul>
      <p class="net-weight">NET WT 360g / 30 SERVINGS | FOOD SUPPLEMENT</p>
    </article>
  </section>
  <section class="stage stage--white">
    <article class="pouch pouch--white">
      <div class="shield"><span class="brand-dot"></span><span class="brand-name">Brindle Cove</span></div>
      <h1 class="product-name"><span class="name-a">TUMB</span><span class="name-b">LAVERA</span></h1>
      <p class="tagline">Collagen Peptides &amp; <span class="tagline-accent">Medicinal Mushrooms</span></p>
      <p class="spec-pill">- TYPE I, II, III | UNFLAVOURED -</p>
      <div class="mushroom-art" role="img" aria-label="Illustration of a cluster of medicinal mushrooms"></div>
      <ul class="claims-band">
        <li class="claim"><span class="claim-mark"></span><span class="claim-label">SUGAR<br>FREE</span></li>
        <li class="claim"><span class="claim-mark"></span><span class="claim-label">GLUTEN<br>FREE</span></li>
        <li class="claim"><span class="claim-mark"></span><span class="claim-label">LAB<br>TESTED</span></li>
        <li class="claim"><span class="claim-mark"></span><span class="claim-label">100%<br>RECYCLABLE</span></li>
      </ul>
      <p class="net-weight">NET WT 360g / 30 SERVINGS | FOOD SUPPLEMENT</p>
    </article>
  </section>
</body>
</html>
```